Letter Head

We need a letter head desgn (A4).
Header Marcus Fennell Creative
phone number 0438571604
email marcusfennellcreative@quillpost.net

Footer ABN 57 314 629 105

```html
<!DOCTYPE html>
<html lang="en">
<head>
<meta charset="utf-8">
<title>Marcus Fennell Creative — Letterhead</title>
<link rel="stylesheet" href="https://fonts.googleapis.com/css2?family=Arimo:wght@400;700&display=swap">
<style>
  :root {
    --paper: #ffffff;
    --green-light: #8fc855;
    --green-mid: #5ab94f;
    --green-deep: #3aae4a;
    --brand-grey: #a7a9ac;
    --brand-green: #39b54a;
    --ink: #231f20;
  }
  * { box-sizing: border-box; margin: 0; padding: 0; }
  html, body {
    width: 847px;
    height: 1200px;
    overflow: hidden;
    background: var(--paper);
  }
  .letterhead {
    position: relative;
    width: 847px;
    height: 1200px;
    background: var(--paper);
    font-family: "Arimo", Arial, Helvetica, sans-serif;
    color: var(--ink);
  }
  .header-band {
    position: absolute;
    top: 0;
    left: 0;
    width: 847px;
    height: 302px;
    background: linear-gradient(110deg, var(--green-light) 0%, var(--green-mid) 45%, var(--green-deep) 70%, var(--green-light) 100%);
    clip-path: polygon(0 0, 847px 0, 847px 302px, 321px 59px, 0 213px);
  }
  .footer-contact {
    position: absolute;
    left: 53px;
    top: 1041px;
    display: flex;
    align-items: flex-start;
    gap: 20px;
  }
  .brand-mark {
    width: 60px;
    height: 60px;
    margin-top: 2px;
    background: var(--brand-grey);
  }
  .contact-details {
    display: flex;
    flex-direction: column;
  }
  .brand-name {
    font-weight: 700;
    font-size: 18.5px;
    line-height: 19px;
    color: var(--brand-grey);
  }
  .brand-tagline {
    font-size: 13px;
    line-height: 13px;
    color: var(--brand-green);
  }
  .contact-phone {
    font-size: 18.5px;
    line-height: 22px;
    margin-top: 1px;
    color: var(--ink);
  }
  .contact-line {
    font-size: 12.5px;
    line-height: 16px;
    color: var(--ink);
  }
</style>
</head>
<body>
  <main class="letterhead">
    <div class="header-band" role="img" aria-label="Green geometric header artwork"></div>

    <footer class="footer-contact">
      <div class="brand-mark"></div>
      <div class="contact-details">
        <p class="brand-name">Marcus Fennell Creative</p>
        <p class="brand-tagline">Photography Video Design</p>
        <p class="contact-phone">0438. 571. 604</p>
        <p class="contact-line">www.mfcreative.com.au</p>
        <p class="contact-line">marcusfennellcreative@quillpost.net</p>
        <p class="contact-line">ABN 57 314 629 105</p>
      </div>
    </footer>
  </main>
</body>
</html>
```